Business Card for Restaurant Business

I represent many restaurants from tiny clam shacks to extraordinary fine dining establishments. I need a business card. I was thinking maybe one that looked like a menu, but I'm open to suggestions. We are in a charming New England resort area (Cape Cod), so something coastal/nautical, but sophisticated.

```html
<!DOCTYPE html>
<html lang="en">
<head>
<meta charset="utf-8">
<title>Harborline Eateries – Business Card</title>
<link href="https://fonts.googleapis.com/css2?family=Arvo&family=Montserrat:wght@400;700&display=swap" rel="stylesheet">
<style>
  :root {
    --backdrop: #d9d9d9;
    --cream: #f1ede4;
    --white: #ffffff;
    --sky-top: #7fb0d6;
    --sky-low: #b9d3e6;
    --dune: #c9b58e;
    --shore: #8d8a6a;
    --sea: #3c7fa6;
    --sea-deep: #2a6688;
    --wood-light: #6a4535;
    --wood-dark: #4a2d22;
    --plank-line: #2f1a13;
    --food-warm: #c97d55;
    --food-light: #e6d7c4;
    --food-dark: #4d4d45;
    --icon-blue: #4a8fc0;
  }
  * { margin: 0; padding: 0; box-sizing: border-box; }
  html, body { width: 1200px; height: 964px; overflow: hidden; background: var(--backdrop); }
  .stage { position: relative; width: 1200px; height: 964px; }

  .card {
    position: absolute;
    left: 276px;
    width: 648px;
    height: 371px;
    border-radius: 18px;
    overflow: hidden;
  }
  .card--front { top: 96px; }
  .card--back { top: 498px; }

  /* Front */
  .harbor-photo {
    position: absolute; inset: 0;
    background: linear-gradient(180deg,
      var(--sky-top) 0%, var(--sky-low) 52%,
      var(--dune) 60%, var(--shore) 74%,
      var(--sea) 80%, var(--sea-deep) 100%);
  }
  .brand-mark {
    position: absolute;
    border-radius: 50%;
    background: var(--white);
  }
  .card--front .brand-mark { left: 66px; top: 39px; width: 116px; height: 116px; }
  .brand-name {
    position: absolute;
    font-family: "Arvo", serif;
    font-weight: 400;
    line-height: 1;
  }
  .card--front .brand-name {
    left: 217px; top: 36px;
    font-size: 58px;
    color: var(--white);
  }
  .brand-name span { display: block; }
  .card--front .brand-name span + span { margin-top: 10px; }

  .social-row {
    position: absolute;
    left: 160px; top: 302px;
    width: 317px; height: 30px;
  }

  /* Back */
  .wood {
    position: absolute; inset: 0;
    background: linear-gradient(90deg, var(--wood-dark), var(--wood-light) 45%, var(--wood-dark));
  }
  .plank-lines { position: absolute; inset: 0; }
  .food-photo {
    position: absolute; inset: 0;
    background: linear-gradient(200deg, var(--food-light) 0%, var(--food-warm) 45%, var(--food-dark) 100%);
    clip-path: polygon(411px 0, 648px 0, 648px 241px, 600px 210px, 520px 120px);
  }
  .card--back .brand-mark { left: 24px; top: 32px; width: 80px; height: 80px; }
  .card--back .brand-name {
    left: 131px; top: 24px;
    font-size: 44px;
    color: var(--cream);
  }
  .card--back .brand-name span + span { margin-top: 6px; }

  .contact-list {
    position: absolute;
    left: 22px; top: 146px;
    list-style: none;
    font-family: "Montserrat", sans-serif;
    font-size: 16px;
    color: var(--white);
  }
  .contact-list li { display: flex; align-items: center; height: 21px; }
  .contact-list svg { width: 14px; height: 14px; margin-right: 6px; flex: none; }

  .address {
    position: absolute;
    left: 22px; top: 285px;
    font-family: "Montserrat", sans-serif;
    font-style: normal;
    font-size: 16px;
    line-height: 21px;
    color: var(--white);
  }
  .person {
    position: absolute;
    right: 23px; top: 305px;
    text-align: right;
    font-family: "Montserrat", sans-serif;
    color: var(--white);
  }
  .person-name { font-weight: 700; font-size: 20px; letter-spacing: 0.5px; line-height: 24px; }
  .person-role { font-size: 16px; line-height: 20px; }
  .accent-bar {
    position: absolute;
    left: 641px; top: 311px;
    width: 7px; height: 37px;
    background: var(--white);
  }
</style>
</head>
<body>
<main class="stage">

  <section class="card card--front">
    <div class="harbor-photo" role="img" aria-label="Photo of a row of coastal cottages on a sandy shore with small boats moored on the bay"></div>
    <div class="brand-mark"></div>
    <h1 class="brand-name"><span>Harborline</span><span>Eateries</span></h1>
    <svg class="social-row" viewBox="0 0 317 30" aria-label="Social media links">
      <g fill="none" stroke="#ffffff" stroke-width="3">
        <line x1="0" y1="15" x2="60" y2="15"/>
        <line x1="257" y1="15" x2="317" y2="15"/>
      </g>
      <g fill="#ffffff">
        <circle cx="87" cy="15" r="15"/>
        <circle cx="126" cy="15" r="15"/>
        <circle cx="164" cy="15" r="15"/>
        <circle cx="203" cy="15" r="15"/>
        <circle cx="239" cy="15" r="15"/>
      </g>
    </svg>
  </section>

  <section class="card card--back">
    <div class="wood" role="img" aria-label="Dark stained wooden planks"></div>
    <svg class="plank-lines" viewBox="0 0 648 371" aria-hidden="true">
      <g stroke="#2f1a13" stroke-width="3">
        <line x1="0" y1="26" x2="648" y2="26"/>
        <line x1="0" y1="112" x2="648" y2="112"/>
        <line x1="0" y1="250" x2="648" y2="250"/>
        <line x1="0" y1="316" x2="648" y2="316"/>
      </g>
    </svg>
    <div class="food-photo" role="img" aria-label="Photo of a seafood rice dish with shrimp and vegetables"></div>

    <div class="brand-mark"></div>
    <h2 class="brand-name"><span>Harborline</span><span>Eateries</span></h2>

    <ul class="contact-list">
      <li>
        <svg viewBox="0 0 14 14" fill="none" stroke="#fff" stroke-width="1.4"><rect x="4" y="1" width="6" height="12" rx="1"/><line x1="6" y1="11" x2="8" y2="11"/></svg>
        508.214.0172
      </li>
      <li>
        <svg viewBox="0 0 14 14" fill="#fff"><path d="M3 1l2.5 3-1.5 1.5c.8 1.8 2.2 3.2 4 4L9.5 8 13 10.5 11.5 13C6 12.5 1.5 8 1 2.5z"/></svg>
        508.214.0185
      </li>
      <li>
        <svg viewBox="0 0 14 14" fill="#fff"><rect x="3" y="1" width="8" height="4"/><rect x="1" y="5" width="12" height="6" rx="1"/><rect x="3" y="9" width="8" height="4"/></svg>
        508.214.0196
      </li>
      <li>
        <svg viewBox="0 0 14 14" fill="#fff"><rect x="1" y="3" width="12" height="8" rx="1"/><path d="M1.5 3.5L7 8l5.5-4.5" stroke="#4a2d22" stroke-width="1.2" fill="none"/></svg>
        hello@harborlinemail.com
      </li>
      <li>
        <svg viewBox="0 0 14 14" fill="none" stroke="#fff" stroke-width="1.3"><circle cx="7" cy="7" r="5.6"/><ellipse cx="7" cy="7" rx="2.4" ry="5.6"/><line x1="1.4" y1="7" x2="12.6" y2="7"/></svg>
        www.harborlineeateries.com
      </li>
    </ul>

    <address class="address">
      1820 Shoreview Lane<br>
      P.O. Box 410226<br>
      Wellfleet, MA 02667
    </address>

    <div class="person">
      <p class="person-name">ELLIOT MARSH</p>
      <p class="person-role">Director</p>
    </div>
    <div class="accent-bar"></div>
  </section>

</main>
</body>
</html>
```